Corporate Identity Design Project

Marisol Tevendry Design is a small boutique event planning and floral design company, based in Northern Alberta. I require the creation of some corporate identity pieces. I want a minimalistic design.
Website www.marisoltevendry.com

Pieces should include
1. Business Card
Should include the company logo, name, email address, address, phone number. These will be professional printed.
These are three cards that I like:
http://cardlayoutgallerynook.com/wp-content/uploads/2010/02/Renata_Voskuilen_Roomworks_by_Pepperleaf_studio_Graphics.jpg
http://tidycardshowcase.com/wp-content/uploads/2011/06/Quietfold-Studio-Minimalist-Business-Cards_11.jpg
http://graphiclanternhub.com/wp-content/uploads/2012/03/16.minimalist-business-cards.jpg
I like letterpress, but I am open to other options.

2. Letterhead
will be professionally printed

3. Envelope

4. Fax Sheet
will be printed on home printer

5. Pocket Presentation
Like -http://fernwickgardenworks.com/img/design_step_proposal@2x.jpg

6. Invoice
Like - http://velmaquorlin.files.blogsite-example.com/2011/02/summit-strength-4-letterhead-combined.png?w=529

7. Proposal
Like something like this – this will not be printed, but rather emailed to clients
Like http://getfile7.brindlepost.com/getfile/files.brindlepost.com/tarnu-studio/qwRtZe8MmXp3LoKcV7B2nhdYJsaWeFUy6gT4rkPHvxiQbNcDzA9jsLE/Picture-52.png.scaled.500.jpg

8. Contract
Like http://www.brightkeelpromo.co.uk/images/tamsin-contract.jpg

9. Business Brochure – I have removed this piece from the project and will most likely post it as another project at a later date.

If you think that this is a project of interest to you, but feel that it is “too much” work for the price, please let me know how you would re-package it – I am open to suggestions.

Target Market(s)

Young women

Industry/Entity Type

Boutique

Requirements
Should not have
• I do not want it to look "frilly"

```html
<!DOCTYPE html>
<html lang="en">
<head>
<meta charset="utf-8">
<title>Marisol Tevendry Design — Stationery Set</title>
<link href="https://fonts.googleapis.com/css2?family=Open+Sans:wght@400;600&display=swap" rel="stylesheet">
<style>
  :root {
    --backdrop: #a3835c;
    --paper: #ffffff;
    --ink: #4f4b48;
    --rose: #b4656f;
    --gold-deep: #e4cd9c;
    --gold-light: #faf3e2;
  }
  * { margin: 0; padding: 0; box-sizing: border-box; }
  html, body { width: 1200px; height: 773px; overflow: hidden; }
  body {
    position: relative;
    background: var(--backdrop);
    font-family: "Open Sans", Arial, sans-serif;
    color: var(--ink);
  }
  .brand {
    position: absolute;
    display: flex;
    align-items: center;
    gap: 10px;
  }
  .brand-dot {
    flex: none;
    border-radius: 50%;
    background: var(--rose);
  }
  .brand-name {
    font-weight: 600;
    color: var(--ink);
    text-transform: uppercase;
    line-height: 1.15;
    letter-spacing: 0.12em;
  }
  .hero-brand { left: 110px; top: 300px; gap: 22px; }
  .hero-brand .brand-dot { width: 86px; height: 86px; }
  .hero-brand .brand-name { font-size: 30px; }

  .letterhead {
    position: absolute;
    left: 432px; top: 40px;
    width: 486px; height: 688px;
    background: var(--paper);
  }
  .letterhead .brand { left: 24px; top: 32px; }
  .letterhead .brand-dot { width: 26px; height: 26px; }
  .letterhead .brand-name { font-size: 9px; }
  .letterhead-band {
    position: absolute;
    left: 156px; top: 58px;
    width: 330px; height: 30px;
    background: linear-gradient(90deg, var(--gold-deep), var(--gold-light));
  }
  .contact {
    font-size: 10px;
    line-height: 1.35;
    color: var(--ink);
  }
  .contact li { list-style: none; display: flex; align-items: center; gap: 6px; }
  .contact svg { width: 9px; height: 9px; flex: none; }
  .contact .web { font-weight: 600; }
  .letterhead-contact {
    position: absolute;
    right: 10px; bottom: 8px;
    padding-right: 8px;
    border-right: 5px solid var(--rose);
  }

  .envelope {
    position: absolute;
    left: 606px; top: 402px;
    width: 558px; height: 262px;
    background: var(--paper);
  }
  .envelope .brand { left: 18px; top: 176px; }
  .envelope .brand-dot { width: 26px; height: 26px; }
  .envelope .brand-name { font-size: 9px; }
  .envelope-band {
    position: absolute;
    left: 140px; top: 194px;
    width: 418px; height: 52px;
    padding: 5px 0 0 14px;
    border-left: 6px solid var(--rose);
    background: linear-gradient(90deg, var(--gold-deep), var(--gold-light));
  }

  .card {
    position: absolute;
    top: 254px;
    height: 124px;
    background: linear-gradient(160deg, var(--gold-light), var(--gold-deep));
  }
  .card-front { left: 728px; width: 192px; }
  .card-front .brand { left: 100px; top: 60px; gap: 6px; }
  .card-front .brand-dot { width: 20px; height: 20px; }
  .card-front .brand-name { font-size: 7px; }
  .card-front-strip {
    position: absolute;
    left: 92px; bottom: 0;
    width: 100px; height: 5px;
    background: var(--rose);
  }
  .card-back { left: 952px; width: 212px; }
  .card-back .contact {
    position: absolute;
    left: 78px; top: 84px;
    font-size: 6.5px;
  }
  .card-back .contact svg { width: 6px; height: 6px; }
  .card-back .contact .web { color: var(--rose); border-bottom: 2px solid var(--rose); }
</style>
</head>
<body>

  <div class="brand hero-brand">
    <span class="brand-dot"></span>
    <span class="brand-name">Marisol<br>Tevendry<br>Design</span>
  </div>

  <section class="letterhead" aria-label="Letterhead">
    <div class="brand">
      <span class="brand-dot"></span>
      <span class="brand-name">Marisol<br>Tevendry<br>Design</span>
    </div>
    <div class="letterhead-band"></div>
    <ul class="contact letterhead-contact">
      <li>Lenmore, Calvaria, Norwend.</li>
      <li><svg viewBox="0 0 10 10"><path d="M2 1l2 2-1 1.2c.6 1.2 1.5 2.1 2.8 2.8L7 6l2 2-1.4 1.4C4.5 9 1 5.5.6 2.4z" fill="currentColor"/></svg>000 000 0000</li>
      <li><svg viewBox="0 0 10 10"><rect x=".5" y="2" width="9" height="6" fill="none" stroke="currentColor"/><path d="M.5 2l4.5 3.5L9.5 2" fill="none" stroke="currentColor"/></svg>hello@marisoltevendry.com</li>
      <li class="web">www.marisoltevendry.com</li>
    </ul>
  </section>

  <section class="card card-front" aria-label="Business card front">
    <div class="brand">
      <span class="brand-dot"></span>
      <span class="brand-name">Marisol<br>Tevendry<br>Design</span>
    </div>
    <div class="card-front-strip"></div>
  </section>

  <section class="card card-back" aria-label="Business card back">
    <ul class="contact">
      <li>Lenmore, Calvaria, Norwend.</li>
      <li><svg viewBox="0 0 10 10"><path d="M2 1l2 2-1 1.2c.6 1.2 1.5 2.1 2.8 2.8L7 6l2 2-1.4 1.4C4.5 9 1 5.5.6 2.4z" fill="currentColor"/></svg>000 000 0000</li>
      <li><svg viewBox="0 0 10 10"><rect x=".5" y="2" width="9" height="6" fill="none" stroke="currentColor"/><path d="M.5 2l4.5 3.5L9.5 2" fill="none" stroke="currentColor"/></svg>hello@marisoltevendry.com</li>
      <li class="web">www.marisoltevendry.com</li>
    </ul>
  </section>

  <section class="envelope" aria-label="Envelope">
    <div class="brand">
      <span class="brand-dot"></span>
      <span class="brand-name">Marisol<br>Tevendry<br>Design</span>
    </div>
    <ul class="contact envelope-band">
      <li>Lenmore, Calvaria, Norwend.</li>
      <li><svg viewBox="0 0 10 10"><path d="M2 1l2 2-1 1.2c.6 1.2 1.5 2.1 2.8 2.8L7 6l2 2-1.4 1.4C4.5 9 1 5.5.6 2.4z" fill="currentColor"/></svg>000 000 0000</li>
      <li><svg viewBox="0 0 10 10"><rect x=".5" y="2" width="9" height="6" fill="none" stroke="currentColor"/><path d="M.5 2l4.5 3.5L9.5 2" fill="none" stroke="currentColor"/></svg>hello@marisoltevendry.com</li>
      <li class="web">www.marisoltevendry.com</li>
    </ul>
  </section>

</body>
</html>
```